New Company Business Card Design

I have a new company logo and I want a new business card design. I dont know if the logo file i attached is in the correct format or quality. We are a New York City Specialty construction Firm specializing in high risk out of the box projects. I want a simple and classy business card that people will his card is as crisp as the work his company does.

Target Market(s)

Clients in the heavy construction industry in New York City

Industry/Entity Type

Construction Company

Contact Information for Business Card

Simple Classy - DIFFERENT

Font styles to use
Other font styles liked:
• Mach the logo font in some way

Colors

Designer to choose colors to be used in the design.

Requirements
Must have
• Uniqueness
Nice to have
• Nothing particular - Just different and classy - Timeless
Should not have
• Goofy Shit or Gimmicky shit

```html
<!DOCTYPE html>
<html lang="en">
<head>
<meta charset="utf-8">
<title>KDR.COM Business Card</title>
<link rel="stylesheet" href="https://fonts.googleapis.com/css2?family=Oswald:wght@600&display=swap">
<style>
  :root {
    --card-white: #ffffff;
    --sky-blue: #1f9ad8;
    --deep-blue: #0d5ea8;
    --brand-blue: #1a74bb;
    --charcoal: #333234;
    --ink: #0a0a0a;
  }
  * { margin: 0; padding: 0; box-sizing: border-box; }
  html, body {
    width: 1200px;
    height: 647px;
    overflow: hidden;
    background: var(--card-white);
  }
  .card {
    position: relative;
    width: 1200px;
    height: 647px;
    background: var(--card-white);
    font-family: "Oswald", "Arial Narrow", sans-serif;
    font-weight: 600;
    overflow: hidden;
  }
  .card-shapes {
    position: absolute;
    inset: 0;
    width: 1200px;
    height: 647px;
  }
  .shape-left { fill: var(--sky-blue); }
  .shape-stripe { fill: var(--deep-blue); }
  .shape-corner { fill: var(--charcoal); }

  .line {
    position: absolute;
    line-height: 1;
    white-space: nowrap;
    text-transform: uppercase;
  }
  .company-name {
    left: 196px;
    top: 44px;
    font-size: 72px;
    letter-spacing: 2px;
    color: var(--brand-blue);
  }
  .company-label {
    left: 154px;
    top: 186px;
    font-size: 37px;
    color: var(--brand-blue);
  }
  .address-street {
    left: 327px;
    top: 240px;
    font-size: 35px;
    color: var(--ink);
  }
  .address-city {
    right: 202px;
    top: 296px;
    font-size: 35px;
    color: var(--ink);
  }
  .office-phone {
    right: 194px;
    top: 361px;
    font-size: 41px;
    letter-spacing: 1px;
    color: var(--ink);
  }
  .person-name {
    left: 244px;
    top: 452px;
    font-size: 34px;
    color: var(--brand-blue);
  }
  .person-email {
    right: 165px;
    top: 499px;
    font-size: 41px;
    letter-spacing: 1.5px;
    color: var(--ink);
  }
  .person-phone {
    right: 109px;
    top: 572px;
    font-size: 41px;
    letter-spacing: 1px;
    color: var(--ink);
  }
</style>
</head>
<body>
  <div class="card">
    <svg class="card-shapes" viewBox="0 0 748 403" preserveAspectRatio="none" aria-hidden="true">
      <polygon class="shape-left" points="0,0 33,0 160,403 0,403"/>
      <polygon class="shape-corner" points="588,0 748,0 748,392"/>
      <polygon class="shape-stripe" points="562,0 588,0 748,392 748,403 730,403"/>
    </svg>

    <div class="line company-name">KDR.COM</div>

    <div class="line company-label">Company</div>
    <div class="line address-street">Address: 418 Harbor Point Road</div>
    <div class="line address-city">Linden, New Jersey 07036</div>
    <div class="line office-phone">Phone: 908-555-0142</div>

    <div class="line person-name">Marco R. Castell</div>
    <div class="line person-email">Email: marco@kdr.com</div>
    <div class="line person-phone">Phone: 917-555-0187</div>
  </div>
</body>
</html>
```